Popup Nightclub Grand Opening Flyer

We need to design a flyer for the grand opening of an upscale, exclusive nightclub called "Lanternfall". The design needs to be chic and exclusive. The background should be black and the text should primarily be white. We like minimalist designs.

Here is the text for the flyer
-
Velvetroom Atlanta Presents

Lanternfall (LOGO)

A Popup Nightclub Experience
For one night Only

Friday, October 18, 2013
Party begins at 9PM

INVITE ONLY

See invitation for location details
(Velvetroom Atlanta logo)

-
Examples we like

http://cdn2-b.plorvex-news.test/sites/default/files/styles/image_content_width/hash/3d/fb/4729105836_5521_flyer.jpg?itok=Q8rmZt2w

http://api.trevlomesh.test/files/9Kxq-Tr72PQd0hzXbwaLr8VMN2K617J3nqBw5CHR4XtdM8Y2sqEA-KjuxBnRoLW4QTyMHD8nwfYcJz-Rkh3vqp4MNaTYe9s1/7zenFridays.jpg

http://brenquist.test/wp-content/uploads/yootheme/widgetkit/gallery/7zen/7zen-gen_nvibe4-01.jpg
Updates

Hi All, one thing that we are seeing that we don't like is on over emphasis on the phrase "a popup nightclub experience" please don't make this the largest thing on the flyer

Target Market(s)

Target market is 25-35 year olds who are affluent (rich) and like luxury brands

Requirements
Must have
• Dark Background
Nice to have
• Velvetroom Logo on the bottom
Modern text that isn't curvy
Should not have
• Curved text

```html
<!DOCTYPE html>
<html lang="en">
<head>
<meta charset="utf-8">
<title>Lanternfall Nightclub — Velvetroom Atlanta</title>
<link rel="stylesheet" href="https://fonts.googleapis.com/css2?family=Jost:wght@300;400;500;600&display=swap">
<style>
  :root {
    --ink-deep: #0d0a24;
    --ink-violet: #2a1647;
    --ink-plum: #4b1239;
    --ink-crimson: #6b0f2a;
    --ink-teal: #0f2a3a;
    --light-text: #e3ebf7;
    --glow: rgba(170, 200, 255, 0.75);
    --streak-white: rgba(235, 240, 255, 0.85);
    --streak-blue: rgba(140, 180, 230, 0.55);
    --streak-pink: rgba(240, 170, 200, 0.55);
  }
  * { margin: 0; padding: 0; box-sizing: border-box; }
  html, body {
    width: 1200px; height: 1080px; overflow: hidden;
    background: var(--ink-deep);
  }
  .flyer {
    position: relative;
    width: 1200px; height: 1080px; overflow: hidden;
    font-family: "Jost", "Futura", sans-serif;
    color: var(--light-text);
    background:
      radial-gradient(ellipse 700px 600px at 100% 5%, var(--ink-crimson) 0%, transparent 70%),
      radial-gradient(ellipse 800px 700px at 85% 70%, var(--ink-plum) 0%, transparent 75%),
      radial-gradient(ellipse 700px 700px at 0% 80%, var(--ink-teal) 0%, transparent 75%),
      linear-gradient(160deg, #171338 0%, var(--ink-violet) 45%, #24102e 100%);
  }
  .light-streaks {
    position: absolute; left: 0; top: 260px; width: 1200px; height: 600px;
    background:
      radial-gradient(ellipse 380px 70px at 90px 270px, var(--streak-white) 0%, transparent 70%),
      radial-gradient(ellipse 520px 120px at 260px 280px, var(--streak-blue) 0%, transparent 70%),
      radial-gradient(ellipse 500px 90px at 700px 240px, var(--streak-pink) 0%, transparent 72%),
      radial-gradient(ellipse 420px 60px at 1050px 170px, var(--streak-pink) 0%, transparent 72%),
      radial-gradient(ellipse 600px 110px at 500px 330px, rgba(200, 190, 240, 0.35) 0%, transparent 72%);
    transform: rotate(-8deg);
    filter: blur(6px);
  }
  .line {
    position: absolute; left: 0; width: 1200px;
    text-align: center; text-transform: uppercase;
    text-shadow: 0 0 10px var(--glow), 0 0 22px rgba(150, 180, 255, 0.45);
  }
  .presenter { top: 52px; font-size: 26px; font-weight: 500; letter-spacing: 3px; }
  .brand-mark {
    position: absolute; left: 538px; top: 134px;
    width: 124px; height: 124px; border-radius: 50%;
    border: 14px solid var(--light-text);
  }
  .brand-name {
    position: absolute; left: 0; width: 1200px; text-align: center;
    font-weight: 300; color: var(--light-text); text-transform: uppercase;
  }
  .brand-name.main { top: 342px; font-size: 60px; letter-spacing: 10px; line-height: 1; }
  .brand-name.sub { top: 414px; font-size: 29px; letter-spacing: 6px; line-height: 1; }
  .tagline { top: 512px; font-size: 39px; font-weight: 600; letter-spacing: 1.5px; line-height: 54px; }
  .rule {
    position: absolute; height: 3px; background: var(--light-text);
    box-shadow: 0 0 8px var(--glow);
  }
  .rule.wide { left: 314px; top: 626px; width: 536px; }
  .date { top: 656px; font-size: 38px; font-weight: 300; letter-spacing: 2px; line-height: 44px; }
  .start { top: 698px; font-size: 38px; font-weight: 400; letter-spacing: 4px; line-height: 44px; }
  .invite { top: 774px; font-size: 38px; font-weight: 600; letter-spacing: 1.5px; line-height: 44px; }
  .rule.left { left: 330px; top: 795px; width: 116px; }
  .rule.right { left: 736px; top: 795px; width: 116px; }
  .location { top: 872px; font-size: 25px; font-weight: 500; letter-spacing: 2.5px; line-height: 32px; }
  .host-name {
    position: absolute; left: 0; width: 1200px; top: 956px;
    text-align: center; font-size: 34px; font-weight: 400;
    letter-spacing: 3px; color: var(--light-text); text-transform: uppercase;
  }
</style>
</head>
<body>
  <main class="flyer">
    <div class="light-streaks" role="img" aria-label="Soft sweeping ribbons of white, blue and pink light across the dark background"></div>

    <p class="line presenter">Velvetroom Atlanta Presents</p>

    <div class="brand-mark" aria-hidden="true"></div>
    <h1 class="brand-name main">Lanternfall</h1>
    <p class="brand-name sub">Nightclub</p>

    <p class="line tagline">A Popup Nightclub Experience<br>For One Night Only</p>
    <div class="rule wide"></div>

    <p class="line date">Friday, October 18, 2013</p>
    <p class="line start">Party Begins at 9PM</p>

    <div class="rule left"></div>
    <p class="line invite">Invite Only</p>
    <div class="rule right"></div>

    <p class="line location">See Invitation for Location Details</p>

    <p class="host-name">Velvetroom Atlanta</p>
  </main>
</body>
</html>
```